Business Card Design Project

Hello- I am an interior stylist/product designer whose work is detail driven, very clean and transitional in style and I want my business card to reflect those qualities. I have a logo that I use on my website- my name and a hand drawn chandelier that I want incorporated into the design. However, "Design for the Home" needs to be changed to "Designs". I will be using cream colored stock and am thinking of gray text and logo. I need your help in pulling my card together since it will be the most used element and drive the design of the rest of my stationary suite.
Updates

Please note that I have changed my QR code from my cell # to my website. The new code will be downloaded now.

Reason: I want to thank everyone who has submitted designs- there are truly some very inspiring designs and I am very pleased. I want to make certain that I get this right and have an attractive and highly effective marketing tool when we are finished. With that said, I have run into a technical problem with one aspect of the card- a qr code for my website that was not part of the original brief. I will get that corrected today and post. Once I get that taken care of, I will post comments to all designs received do far. Thanks again for everyone's efforts, Risa

QR Code for the website is now uploaded. Thanks for your patience!

Target Market(s)

Upper middle class- mostly women

Industry/Entity Type

Business

Requirements
Must have
• Marisa Vantry Designs
"...to the last detail."
214-555-0148
marisavantry@plumwick.net
www.marisavantrydesigns-example.com
27083 Birchmont Court
Dallas, TX 75000
Nice to have
• Risa Vantry
Owner

```html
<!DOCTYPE html>
<html lang="en">
<head>
<meta charset="utf-8">
<title>Marisa Vantry Designs — Business Card</title>
<link rel="stylesheet" href="https://fonts.googleapis.com/css2?family=Open+Sans:ital,wght@0,400;0,700;1,400&display=swap">
<style>
  :root {
    --backdrop: #e9e6e1;
    --cream: #fce8c4;
    --band-gray: #58585a;
    --ink: #5d5751;
    --logo-ink: #6e665d;
    --white: #ffffff;
    --shadow: rgba(40, 30, 20, 0.22);
  }
  * { box-sizing: border-box; margin: 0; padding: 0; }
  html, body {
    width: 1200px; height: 758px; overflow: hidden;
    background: var(--backdrop);
    font-family: "Open Sans", Arial, sans-serif;
  }
  .sheet {
    position: relative; width: 1200px; height: 758px;
    display: flex; align-items: center; justify-content: center; gap: 60px;
  }
  .card {
    position: relative; width: 520px; height: 300px;
    border-radius: 22px; background: var(--cream);
    box-shadow: 0 10px 24px var(--shadow);
    overflow: hidden; color: var(--ink);
  }
  /* front */
  .card-front { display: flex; flex-direction: column; }
  .band-top {
    height: 52px; background: var(--band-gray); color: var(--white);
    display: flex; align-items: center; justify-content: center; gap: 5px;
  }
  .owner-name { font-weight: 700; font-size: 17px; }
  .owner-title { font-size: 12px; }
  .brand-block {
    flex: 1; display: flex; flex-direction: column;
    align-items: center; justify-content: center; text-align: center;
  }
  .brand-name {
    display: flex; align-items: center; gap: 10px;
    font-size: 34px; font-weight: 400; color: var(--logo-ink); line-height: 1;
  }
  .brand-dot {
    width: 12px; height: 12px; border-radius: 50%; background: var(--logo-ink);
  }
  .brand-sub { margin-top: 8px; font-size: 12px; letter-spacing: 0.5px; }
  .tagline { font-size: 13px; font-style: italic; }
  .band-bottom {
    height: 100px; background: var(--band-gray); color: var(--white);
    display: flex; flex-direction: column; align-items: center; justify-content: center;
    gap: 6px; font-size: 12px;
  }
  .contact-row { display: flex; align-items: center; gap: 14px; }
  .contact-item { display: flex; align-items: center; gap: 5px; }
  .contact-item svg { width: 11px; height: 11px; fill: var(--white); }
  .address { font-size: 13px; margin-top: 4px; }
  /* back */
  .card-back {
    display: flex; flex-direction: column; align-items: center; justify-content: center;
    gap: 44px;
  }
  .brand-name-large {
    display: flex; align-items: center; gap: 14px;
    font-size: 50px; font-weight: 400; color: var(--logo-ink); line-height: 1;
  }
  .brand-name-large .brand-dot { width: 16px; height: 16px; }
  .back-web { font-size: 17px; font-weight: 700; color: var(--band-gray); }
</style>
</head>
<body>
<main class="sheet">
  <section class="card card-front" aria-label="Business card front">
    <header class="band-top">
      <span class="owner-name">Risa Vantry,</span>
      <span class="owner-title">Owner</span>
    </header>
    <div class="brand-block">
      <div class="brand-name"><span>Marisa</span><span class="brand-dot"></span><span>Vantry</span></div>
      <div class="brand-sub">DESIGNS</div>
      <div class="tagline">"...to the last detail"</div>
    </div>
    <footer class="band-bottom">
      <div class="contact-row">
        <span class="contact-item">
          <svg viewBox="0 0 24 24" aria-hidden="true"><path d="M6.6 10.8a15.1 15.1 0 0 0 6.6 6.6l2.2-2.2c.3-.3.7-.4 1-.2 1.1.4 2.3.6 3.6.6.6 0 1 .4 1 1V20c0 .6-.4 1-1 1A17 17 0 0 1 3 4c0-.6.4-1 1-1h3.5c.6 0 1 .4 1 1 0 1.3.2 2.5.6 3.6.1.3 0 .7-.2 1z"/></svg>
          214-555-0148
        </span>
        <span class="contact-item">
          <svg viewBox="0 0 24 24" aria-hidden="true"><path d="M2 5h20v14H2z M2 5l10 7 10-7" /></svg>
          marisavantry@plumwick.net
        </span>
      </div>
      <div class="contact-item">
        <svg viewBox="0 0 24 24" aria-hidden="true"><circle cx="12" cy="12" r="10"/></svg>
        www.marisavantrydesigns-example.com
      </div>
      <div class="address">27083 Birchmont Court, Dallas, TX 75000</div>
    </footer>
  </section>

  <section class="card card-back" aria-label="Business card back">
    <div class="brand-name-large"><span>Marisa</span><span class="brand-dot"></span><span>Vantry</span></div>
    <div class="back-web">www.marisavantrydesigns-example.com</div>
  </section>
</main>
</body>
</html>
```